Ringordner
Zielgruppe
Wir sind ein ambulanter Pflegedienst, der im Raum Dessau-Roßlau tätig ist. Wir haben uns mit einer Tagespflege erweitert. Zukünftig ist es geplant, dass wir uns um eine Therapie erweitern. Unsere Zielgruppe sind sämtliche Pflegebedürftige und deren Angehörige. Für die aktuelle Maßnahme sind jedoch die zukünftigen Mitarbeiter im Vordergrund.
Aufgabenstellung
Ich möchte für unsere zukünftigen Mitarbeiter einen A4 Ringordner mit zwei Klammern gestalten. Dieser Ordner wird als Willkomm Mappe für neue Mitarbeiter bei der Aufnahme der Tätigkeit übergeben. Das Design sollte das Hauptlogo des Pflegedienstes enthalten und auf die Tochterfirmen hinweisen. Es sollte modern und frisch wirken und vor allem professionell. Es soll die Mitarbeiter in unserer neuen Firma willkommen heißen.
Dann benötige ich ein zweites Design, dass für die Kunden ist. Es beinhaltet einen Leitfaden, was für die Zusammenarbeit zwischen Pflegedienst und Patient am wichtigsten ist. Dieses Design ist genauso wie beim Mitarbeiter ein A4 Ringordner mit zwei Klammern. Auch dieser Ordner soll diesmal den Patienten bekommen heißen. Hier soll auch das Logo des Pflegedienstes enthalten sein und auch die Tochterfirmen hinweisen.

```html
<!DOCTYPE html>
<html lang="de">
<head>
<meta charset="utf-8">
<title>Elbauen Betreuung – Willkommensordner</title>
<link href="https://fonts.googleapis.com/css2?family=Montserrat:wght@400;500;600;700&family=Playfair+Display:wght@500&display=swap" rel="stylesheet">
<style>
  :root {
    --page-bg: #e6e6e6;
    --cover-top: #eceee8;
    --cover-bottom: #cde6e5;
    --accent-teal: #39b1ad;
    --deep-teal: #2a7b72;
    --text-grey: #7a7a7a;
    --partner-peach: #e59b63;
    --card-bg: rgba(255, 255, 255, 0.82);
    --icon-bg: #d6efee;
    --band-blue: #37a6de;
    --band-blue-dark: #2c97d4;
    --photo-light: #e7eef0;
    --photo-mid: #c9dbe0;
    --white: #ffffff;
  }
  * { box-sizing: border-box; margin: 0; padding: 0; }
  html, body {
    width: 1200px;
    height: 1040px;
    overflow: hidden;
    background: var(--page-bg);
    font-family: "Montserrat", sans-serif;
  }
  .binder-cover {
    position: absolute;
    left: 160px;
    top: 20px;
    width: 880px;
    height: 1000px;
    overflow: hidden;
    background: linear-gradient(170deg, var(--cover-top) 0%, #e3ece8 45%, var(--cover-bottom) 100%);
  }
  .partner-mark {
    position: absolute;
    left: 34px;
    top: 36px;
    display: flex;
    align-items: center;
    gap: 10px;
  }
  .partner-mark .dot {
    width: 30px;
    height: 30px;
    border-radius: 50%;
    background: var(--partner-peach);
    opacity: 0.85;
  }
  .partner-mark .name {
    font-size: 15px;
    font-weight: 500;
    letter-spacing: 0.04em;
    color: var(--partner-peach);
  }
  .brand-block {
    position: absolute;
    top: 40px;
    left: 0;
    width: 100%;
    text-align: center;
  }
  .brand-block .brand-dot {
    display: block;
    width: 58px;
    height: 58px;
    margin: 0 auto 10px;
    border-radius: 50%;
    background: var(--accent-teal);
  }
  .brand-block .brand-name {
    font-size: 30px;
    font-weight: 600;
    letter-spacing: 0.01em;
    color: var(--deep-teal);
  }
  .headline {
    position: absolute;
    top: 150px;
    left: 0;
    width: 100%;
    text-align: center;
  }
  .headline .lead {
    font-family: "Playfair Display", serif;
    font-size: 28px;
    font-weight: 500;
    color: var(--deep-teal);
  }
  .headline .main {
    font-size: 46px;
    font-weight: 700;
    color: var(--accent-teal);
    line-height: 1.1;
  }
  .intro {
    position: absolute;
    top: 262px;
    left: 110px;
    width: 660px;
    text-align: center;
    font-size: 15px;
    line-height: 1.45;
    color: var(--text-grey);
  }
  .benefits {
    position: absolute;
    top: 380px;
    left: 33px;
    display: flex;
    gap: 18px;
  }
  .benefit-card {
    width: 190px;
    height: 128px;
    border-radius: 14px;
    background: var(--card-bg);
    box-shadow: 0 4px 14px rgba(60, 110, 110, 0.08);
    display: flex;
    flex-direction: column;
    align-items: center;
    padding-top: 20px;
  }
  .benefit-card .icon {
    width: 42px;
    height: 42px;
    border-radius: 50%;
    background: var(--icon-bg);
    display: flex;
    align-items: center;
    justify-content: center;
    margin-bottom: 12px;
  }
  .benefit-card .label {
    font-size: 14px;
    font-weight: 600;
    color: var(--deep-teal);
    text-align: center;
    line-height: 1.25;
  }
  .hero-photo {
    position: absolute;
    left: 90px;
    top: 540px;
    width: 700px;
    height: 420px;
    border-radius: 200px 200px 0 0;
    background: radial-gradient(ellipse at 50% 40%, var(--photo-light) 0%, var(--photo-mid) 100%);
  }
  .url-band {
    position: absolute;
    left: 0;
    bottom: 0;
    width: 100%;
    height: 62px;
    background: linear-gradient(90deg, var(--band-blue), var(--band-blue-dark));
    display: flex;
    align-items: center;
    padding-left: 130px;
  }
  .url-band .url {
    font-size: 22px;
    font-weight: 500;
    letter-spacing: 0.36em;
    color: var(--white);
  }
</style>
</head>
<body>
  <main class="binder-cover">
    <div class="partner-mark">
      <span class="dot"></span>
      <span class="name">Tagespflege Haus Lindenhof</span>
    </div>

    <header class="brand-block">
      <span class="brand-dot"></span>
      <div class="brand-name">Elbauen Betreuung</div>
    </header>

    <div class="headline">
      <div class="lead">Pflege mit</div>
      <div class="main">Herz &amp; Seele</div>
    </div>

    <p class="intro">Wir wissen, dass zufriedene Mitarbeiter bessere Arbeit leisten. Dies kommt nicht nur unseren Patienten zugute, sondern auch dem Teamgeist.</p>

    <section class="benefits">
      <div class="benefit-card">
        <span class="icon">
          <svg width="20" height="20" viewBox="0 0 20 20" fill="none" stroke="#2a7b72" stroke-width="1.6" stroke-linecap="round">
            <path d="M3 9a7 7 0 0 1 14 0z" fill="#2a7b72"/>
            <path d="M10 9v7a2 2 0 0 1-4 0"/>
          </svg>
        </span>
        <span class="label">Urlaub</span>
      </div>
      <div class="benefit-card">
        <span class="icon">
          <svg width="20" height="20" viewBox="0 0 20 20" fill="none" stroke="#2a7b72" stroke-width="1.6" stroke-linecap="round">
            <rect x="4" y="3" width="12" height="14" rx="2"/>
            <path d="M7 7h6M7 10h6M7 13h4"/>
          </svg>
        </span>
        <span class="label">Sonderleistungen</span>
      </div>
      <div class="benefit-card">
        <span class="icon">
          <svg width="20" height="20" viewBox="0 0 20 20" fill="none" stroke="#2a7b72" stroke-width="1.6" stroke-linejoin="round">
            <rect x="3" y="6" width="14" height="10" rx="2"/>
            <path d="M5 6l8-3 1 3"/>
            <circle cx="13.5" cy="11" r="1" fill="#2a7b72"/>
          </svg>
        </span>
        <span class="label">Überdurchschnittliche<br>Vergütung</span>
      </div>
      <div class="benefit-card">
        <span class="icon">
          <svg width="20" height="20" viewBox="0 0 20 20" fill="none" stroke="#2a7b72" stroke-width="1.6" stroke-linejoin="round">
            <path d="M3 5h5a2 2 0 0 1 2 2v9a2 2 0 0 0-2-2H3z" fill="#2a7b72"/>
            <path d="M17 5h-5a2 2 0 0 0-2 2v9a2 2 0 0 1 2-2h5z"/>
          </svg>
        </span>
        <span class="label">Fort- &amp;<br>Weiterbildungen</span>
      </div>
    </section>

    <div class="hero-photo" role="img" aria-label="Foto: eine jüngere Frau umarmt lächelnd eine ältere Frau, beide in Weiß vor hellem Himmel"></div>

    <footer class="url-band">
      <span class="url">elbauen-betreuung.de</span>
    </footer>
  </main>
</body>
</html>
```